Esthetically Pleasing Core Values and Brand Promise for Accounting Firm

I would like a cohesive design that ties together my core values and brand promise. My firm, Maple Finch Advisory, provides accounting work to small businesses. I prefer modern and clean designs. I want my Core Values and Brand Promise to represent me - sole entrepreneur, married, mother of two kids, modern esthetics, clean lines, organized, colorful (teals, greys, white, yellows)

Industry/Entity Type

Public Accounting

Colors
33b8a4

```html
<!DOCTYPE html>
<html lang="en">
<head>
<meta charset="utf-8">
<title>Maple Finch Advisory – Core Values</title>
<link rel="stylesheet" href="https://fonts.googleapis.com/css2?family=Questrial&family=Urbanist:wght@800&display=swap">
<style>
  :root {
    --backdrop: #4d4d4d;
    --paper: #ffffff;
    --navy: #002244;
    --sky: #00b3f0;
    --wood: #6b4a33;
    --desk-grey: #8a8580;
    --ink: #ffffff;
  }
  html, body {
    margin: 0;
    padding: 0;
    width: 687px;
    height: 1200px;
    overflow: hidden;
    background: var(--backdrop);
  }
  .canvas {
    position: relative;
    width: 687px;
    height: 1200px;
  }
  .artwork {
    position: absolute;
    inset: 0;
    width: 687px;
    height: 1200px;
  }
  .heading {
    position: absolute;
    margin: 0;
    color: var(--ink);
    font-family: "Urbanist", "Questrial", sans-serif;
    font-weight: 800;
    letter-spacing: -0.2px;
  }
  .heading--core {
    right: calc(687px - 519px);
    top: 180px;
    font-size: 33px;
    line-height: 27px;
    text-align: right;
  }
  .heading--promise {
    left: 148px;
    top: 628px;
    width: 242px;
    font-size: 29px;
    line-height: 23px;
    text-align: right;
  }
  .value-list {
    position: absolute;
    margin: 0;
    padding: 0 0 0 0;
    list-style: none;
    color: var(--ink);
    font-family: "Questrial", sans-serif;
    font-size: 10.9px;
    line-height: 14.4px;
  }
  .value-list li {
    position: relative;
    margin-bottom: 14.4px;
  }
  .value-list li::before {
    content: "•";
    position: absolute;
    left: -12px;
  }
  .value-list--first { left: 156px; top: 325px; width: 165px; }
  .value-list--second { left: 201px; top: 482px; width: 250px; }
  .promise-item {
    position: absolute;
    margin: 0;
    color: var(--ink);
    font-family: "Questrial", sans-serif;
    font-size: 10.9px;
    line-height: 14.4px;
    text-align: right;
  }
  .promise-item .dot { margin-right: 6px; }
  .promise-item--tax { left: 283px; top: 711px; width: 245px; }
  .promise-item--accounting { left: 360px; top: 812px; width: 183px; }
</style>
</head>
<body>
<main class="canvas">
  <svg class="artwork" viewBox="0 0 1456 2542" xmlns="http://www.w3.org/2000/svg">
    <defs>
      <linearGradient id="handshakeTones" x1="0" y1="0" x2="1" y2="1">
        <stop offset="0" stop-color="#2a3a3a"/>
        <stop offset="0.45" stop-color="#7a5a40"/>
        <stop offset="1" stop-color="#4a3526"/>
      </linearGradient>
      <linearGradient id="chartTones" x1="0" y1="0" x2="0" y2="1">
        <stop offset="0" stop-color="#6f6a63"/>
        <stop offset="0.45" stop-color="#a89a88"/>
        <stop offset="0.7" stop-color="#1aa6e0" stop-opacity="0.9"/>
        <stop offset="1" stop-color="#00b3f0" stop-opacity="0.6"/>
      </linearGradient>
    </defs>
    <rect class="panel" x="253" y="323" width="950" height="1895" fill="var(--paper)"/>
    <path class="band band--top" fill="var(--sky)"
      d="M563,323 L1033,323 L1203,425 L1203,730 L590,468 Q563,455 563,435 Z"/>
    <path class="band band--bottom" fill="var(--sky)"
      d="M253,1730 L870,2075 Q893,2088 893,2112 L893,2218 L420,2218 L253,2120 Z"/>
    <path class="field" fill="var(--navy)"
      d="M253,465 Q300,445 360,478 L710,703 L707,790 Q712,845 770,878 L1203,1132 L1203,2075 Q1150,2092 1100,2062 L748,1838 L748,1740 Q745,1680 690,1650 L253,1410 Z"/>
    <path class="photo photo--handshake" role="img"
      aria-label="Photo: two business people shaking hands over a desk with a contract and laptop"
      fill="url(#handshakeTones)" stroke="var(--paper)" stroke-width="22" stroke-linejoin="round"
      d="M738,540 Q742,478 800,490 L1203,712 L1203,1108 L800,875 Q728,832 728,760 Z"/>
    <path class="photo-tint" fill="var(--sky)" opacity="0.55"
      d="M880,530 L1203,712 L1203,730 L900,600 Z"/>
    <path class="photo photo--chart" role="img"
      aria-label="Photo: hand pointing a pen at a printed financial bar chart"
      fill="url(#chartTones)"
      d="M253,1435 L700,1680 Q728,1700 728,1750 L720,2010 Q716,2062 680,2055 L253,1812 Z"/>
  </svg>

  <h1 class="heading heading--core">Core<br>Values</h1>

  <ul class="value-list value-list--first">
    <li>Empower – we are dedicated, appreciative and respectful of people's time and purpose.</li>
    <li>Client Focused – we provide a personal service that goes above the standards of professional care.</li>
  </ul>

  <ul class="value-list value-list--second">
    <li>Rectitude – we know the difference between what we have the right to do and what the right thing to do is.</li>
    <li>Relentless – we believe that the longer we try to do our best, the better we become.</li>
  </ul>

  <h2 class="heading heading--promise">Transparency and<br>Dependability</h2>

  <p class="promise-item promise-item--tax"><span class="dot">•</span>Tax - Maple Finch Advisory provides all clients with a trusted tax advisor who provides accuracy in all filings and ensures your compliance with all government agencies.</p>

  <p class="promise-item promise-item--accounting"><span class="dot">•</span>Accounting - Maple Finch Advisory provides all business owners with the financial visibility needed to foster growth and facilitate goals.</p>
</main>
</body>
</html>
```